Modern corporate energy/fuel business need business card design

Business card required for company founder. Korvan Integrated Power is a Australian based modern energy/fuel provider. We offer specialised solutions to businesses using fossil fuels through renewable energy solutions.

I would like one side with specific information (name, address etc)

The other side to be bold, professional company name & logo. Striking.

Target Market(s)

B2B. Transport, mining, councils, environmentalist,

Industry/Entity Type

Petroleum

Contact Information for Business Card

Name; Peter Morrow
Position; Director
Email; pmorrow@korvanse.com.au
Address; PO Box 347, Marsden, QLD, 4132
Website; www.korvanse.com.au

Colors

Designer to choose colors to be used in the design.

Requirements
Must have
• Clean, easy to read, professional & strong theme
Should not have
• too many colours, busy layout,

```html
<!DOCTYPE html>
<html lang="en">
<head>
<meta charset="utf-8">
<title>Korvan Integrated Power – Business Card</title>
<link href="https://fonts.googleapis.com/css2?family=Lato:wght@400;700;900&display=swap" rel="stylesheet">
<style>
  :root {
    --stage: #404040;
    --paper: #ffffff;
    --navy: #21507a;
    --orange: #f47a20;
    --orange-light: #ffa047;
    --orange-deep: #ff6a0d;
    --ink: #4a4a4a;
  }
  * { margin: 0; padding: 0; box-sizing: border-box; }
  html, body { width: 1200px; height: 900px; overflow: hidden; }
  body {
    background: var(--stage);
    font-family: "Lato", Arial, sans-serif;
    position: relative;
  }
  .card {
    position: absolute;
    top: 200px;
    width: 310px;
    height: 501px;
  }
  .card-front {
    left: 253px;
    background: var(--paper);
    border-radius: 60px 0 60px 0;
  }
  .card-back {
    left: 627px;
    background: linear-gradient(180deg, var(--orange-light) 0%, var(--orange) 55%, var(--orange-deep) 100%);
    border-radius: 0 60px 0 60px;
  }
  .brand-dot {
    position: absolute;
    left: 117px;
    top: 78px;
    width: 80px;
    height: 80px;
    border-radius: 50%;
    background: var(--orange);
  }
  .brand {
    position: absolute;
    left: 0;
    width: 100%;
    text-align: center;
    color: var(--navy);
  }
  .brand-name {
    font-weight: 900;
    font-size: 42px;
    letter-spacing: 9px;
    line-height: 1;
    margin-right: -9px;
  }
  .brand-tagline {
    font-weight: 400;
    font-size: 11px;
    letter-spacing: 7px;
    line-height: 1;
    margin-top: 6px;
    margin-right: -7px;
  }
  .card-front .brand { top: 178px; }
  .card-back .brand { top: 393px; left: 8px; }
  .contact {
    position: absolute;
    left: 32px;
    top: 333px;
    color: var(--ink);
    font-size: 15px;
    line-height: 18px;
  }
  .contact-name {
    color: var(--orange);
    font-weight: 700;
    font-size: 18px;
    line-height: 20px;
    text-transform: uppercase;
  }
  .contact-role { margin-bottom: 8px; }
  .contact-address { margin-bottom: 9px; }
  .contact-line { display: flex; align-items: center; gap: 4px; }
  .contact-line svg { width: 12px; height: 12px; flex: none; }
</style>
</head>
<body>

  <section class="card card-front" aria-label="Business card, contact side">
    <div class="brand-dot"></div>
    <div class="brand">
      <div class="brand-name">KORVAN</div>
      <div class="brand-tagline">INTEGRATED POWER</div>
    </div>

    <div class="contact">
      <div class="contact-name">Peter Morrow</div>
      <div class="contact-role">Director</div>
      <div class="contact-address">PO Box 347, Marsden<br>QLD, 4132</div>
      <div class="contact-line">
        <svg viewBox="0 0 12 12" aria-hidden="true">
          <rect x="0.5" y="2" width="11" height="8" rx="1" fill="var(--orange)"/>
          <path d="M1 2.6 L6 6.6 L11 2.6" fill="none" stroke="#fff" stroke-width="1"/>
        </svg>
        <span>pmorrow@korvanse.com.au</span>
      </div>
      <div class="contact-line">
        <svg viewBox="0 0 12 12" aria-hidden="true">
          <circle cx="6" cy="6" r="5.5" fill="var(--orange)"/>
          <path d="M0.8 6 H11.2 M6 0.8 C3.5 3.5 3.5 8.5 6 11.2 M6 0.8 C8.5 3.5 8.5 8.5 6 11.2" fill="none" stroke="#fff" stroke-width="0.8"/>
        </svg>
        <span>www.korvanse.com.au</span>
      </div>
    </div>
  </section>

  <section class="card card-back" aria-label="Business card, brand side">
    <div class="brand">
      <div class="brand-name">KORVAN</div>
      <div class="brand-tagline">INTEGRATED POWER</div>
    </div>
  </section>

</body>
</html>
```